Criação de Apres. Comercial (com dobra) para Limpeza & Serviço para o lar
A empresa queria:
" No mercado desde 2001, a Vento Sereno tem como Missão oferecer aos clientes a mais alta qualidade na prestação de serviço3s e manter a confiabilidade conquistada. Nosso posicionamento é o de parceria, no sentido de ajudar nossos clientes a viabilizar seus objetivos e projetos, mantendo-os focados em sua atividade principal. Serviços personalizados, com Mão-de-obra Terceirizada e bem treinada, acompanhados por constante Supervisão, de acordo com as necessidades e características de cada cliente, detectando pontos de melhoria e execução das tarefas de forma clara e precisa. Auxiliares de Serviços Gerais, Controladores de Acesso, Zeladores, Ascensoristas, Recepcionistas, Jardineiros, Copeiras, Garagistas, Limpadores de Vidro, Auxiliares de Manutenção, Telefonistas, Mensageiros, Auxiliares Administrativos. "

```html
<!DOCTYPE html>
<html lang="pt-BR">
<head>
<meta charset="utf-8">
<title>Vento Sereno — Apresentação Comercial</title>
<link href="https://fonts.googleapis.com/css2?family=Arimo:wght@400;700&display=swap" rel="stylesheet">
<style>
  :root{
    --bg:#e6e6e6;
    --paper:#ffffff;
    --teal:#0f6f78;
    --teal-dark:#0a4e55;
    --band:#3b4549;
    --ink:#2b2b2b;
    --muted:#555a5c;
    --map:#c9cccd;
  }
  *{box-sizing:border-box;margin:0;padding:0}
  html,body{width:1200px;height:1200px;overflow:hidden;background:var(--bg)}
  body{font-family:"Arimo",Arial,sans-serif;color:var(--ink);position:relative}
  .spread{position:absolute;left:50px;top:210px;width:1100px;height:780px;display:flex;box-shadow:0 6px 24px rgba(0,0,0,.18)}
  .panel{position:relative;width:550px;height:780px;background:var(--paper);padding:62px 46px 40px}
  .panel--left{border-right:1px solid #e2e2e2}
  .band-top{position:absolute;left:0;right:0;top:0;height:20px}
  .panel--left .band-top{background:var(--band);border-bottom:5px solid var(--teal)}
  .panel--right .band-top{background:var(--teal);border-bottom:5px solid var(--teal-dark)}
  .band-bottom{position:absolute;left:0;right:0;bottom:0;height:12px;background:var(--teal)}
  .panel--left .band-bottom{background:#d8dadb}
  .section{margin-bottom:20px}
  .section-title{display:flex;align-items:center;gap:10px;font-size:14px;font-weight:700;margin-bottom:12px;color:var(--ink)}
  .section-title .dot{width:18px;height:18px;border-radius:50%;background:var(--teal);flex:none}
  .section-title--caps{text-transform:uppercase;font-size:15px}
  .body-text{font-size:10.5px;line-height:1.45;color:var(--muted);margin-bottom:10px;text-align:justify}
  .map{width:100%;height:170px;margin-top:6px}
  .service-lists{display:flex;gap:40px;margin:0 0 18px 30px}
  .service-lists ul{list-style:none;font-size:9.5px;line-height:1.45;color:var(--muted);width:190px}
  .service-lists li::before{content:"•";color:var(--teal);margin-right:6px}
  .photo-strip{width:100%;height:130px;display:block;margin-bottom:18px}
</style>
</head>
<body>
<main class="spread">
  <section class="panel panel--left">
    <div class="band-top"></div>
    <div class="section">
      <h2 class="section-title"><span class="dot"></span>Sobre Nós</h2>
      <p class="body-text">A Vento Sereno foi fundada no ano de 2001 na cidade de São Paulo atuando sempre com qualidade nas áreas de Serviços Gerais e Multisserviços. Sua principal missão é oferecer aos clientes a mais alta qualidade na prestação de serviços e manter a confiabilidade conquistada de forma que ajudamos nossos clientes a viabilizar seus objetivos e projetos, mantendo-os focados em sua atividade principal.</p>
      <p class="body-text">Entre nossos clientes, sua grande maioria foram conquistados por indicações, o que nos dá mais força para continuarmos com nossos objetivos de trabalho, acreditando que a parceria e o respeito ainda são grandes aliados dentro de um mercado de trabalho tão competitivo.</p>
    </div>
    <div class="section">
      <h2 class="section-title"><span class="dot"></span>Diferenciais</h2>
      <p class="body-text">Profissionalismo e competência técnica, acompanhados de um ambiente atraente e agradável para quem trabalha e para quem nos contrata.</p>
      <p class="body-text">Serviços personalizados, com Mão-de-Obra Terceirizada e bem treinada, acompanhados por constante Supervisão, de acordo com as necessidades e características de cada cliente, detectando pontos de melhoria e execução das tarefas de forma clara e precisa.</p>
      <p class="body-text">Trabalhamos com preço justo e rigor no cumprimento dos prazos, atuando com profissionais uniformizados e bem treinados, supervisão constante, equipamentos e materiais de qualidade, adequados a cada tipo de ambiente e revestimento.</p>
    </div>
    <div class="section">
      <h2 class="section-title section-title--caps"><span class="dot"></span>Área de Atuação</h2>
      <svg class="map" viewBox="0 0 458 170" role="img" aria-label="Mapa cinza das regiões atendidas na Grande São Paulo">
        <rect x="40" y="0" width="378" height="170" rx="10" fill="var(--map)"/>
      </svg>
    </div>
    <div class="band-bottom"></div>
  </section>

  <section class="panel panel--right">
    <div class="band-top"></div>
    <div class="section">
      <h2 class="section-title"><span class="dot"></span>Serviços e Solicite um Orçamento</h2>
      <div class="service-lists">
        <ul>
          <li>Auxiliares de Serviços Gerais</li>
          <li>Controladores de Acesso</li>
          <li>Zeladores</li>
          <li>Ascensoristas</li>
          <li>Recepcionistas</li>
          <li>Jardineiros</li>
        </ul>
        <ul>
          <li>Copeiras</li>
          <li>Garagistas</li>
          <li>Limpadores de Vidro</li>
          <li>Auxiliares de Manutenção</li>
          <li>Telefonistas, Mensageiros</li>
          <li>Auxiliares Administrativos</li>
        </ul>
      </div>
      <svg class="photo-strip" viewBox="0 0 458 130" preserveAspectRatio="none">
        <defs>
          <linearGradient id="ph1" x1="0" y1="0" x2="1" y2="1"><stop offset="0" stop-color="#6c7a5a"/><stop offset="1" stop-color="#3d4a33"/></linearGradient>
          <linearGradient id="ph2" x1="0" y1="0" x2="1" y2="1"><stop offset="0" stop-color="#8a8f93"/><stop offset="1" stop-color="#4a5054"/></linearGradient>
          <linearGradient id="ph3" x1="0" y1="0" x2="1" y2="1"><stop offset="0" stop-color="#7a6a55"/><stop offset="1" stop-color="#3a3129"/></linearGradient>
        </defs>
        <rect x="0" y="0" width="160" height="130" fill="url(#ph1)" role="img" aria-label="Foto de jardineiro cuidando de plantas"/>
        <rect x="150" y="0" width="160" height="130" fill="url(#ph2)" role="img" aria-label="Foto de profissional de limpeza em ambiente corporativo"/>
        <rect x="300" y="0" width="158" height="130" fill="url(#ph3)" role="img" aria-label="Foto de recepcionista atendendo ao telefone"/>
        <polygon points="0,0 90,0 0,70" fill="#fff"/>
        <polygon points="140,130 200,0 215,0 155,130" fill="#fff"/>
        <polygon points="290,130 350,0 365,0 305,130" fill="#fff"/>
        <polygon points="458,130 458,60 390,130" fill="#fff"/>
      </svg>
    </div>
    <div class="section">
      <h2 class="section-title"><span class="dot"></span>Pós Obra</h2>
      <p class="body-text">A Vento Sereno é especialista em Limpeza Pós Obra, uma limpeza pesada com fino acabamento, extremamente detalhada e delicada, procurando identificar os diferentes tipos de revestimentos, acabamentos e sujidades existentes, sendo que atuamos nos grandes escritórios de Arquitetura Corporativa e Residências.</p>
      <p class="body-text">Neste segmento, o serviço é desenvolvido a dar tranquilidade ao contratante, pois sabemos o quão trabalhoso é encerrar uma obra e apresentá-la em condições imediatas de utilização.</p>
      <p class="body-text">Nossas Vistorias Técnicas são realizadas exatamente para verificar a real necessidade de nosso cliente, buscando sempre em conjunto a melhor solução, ajustando custos e adequando o nosso trabalho ao serviço solicitado.</p>
    </div>
    <div class="section">
      <h2 class="section-title"><span class="dot"></span>Solicite um Orçamento</h2>
      <p class="body-text">Entre em contato com a equipe da Vento Sereno pelo e-mail comercial@ventosereno.com.br ou ligue no telefone (11) 4020-7310. Estamos à disposição para atender suas necessidades e esclarecer todas as suas dúvidas.</p>
    </div>
    <div class="band-bottom"></div>
  </section>
</main>
</body>
</html>
```